Ridgeford Masonry- Business Card Design

We need a business card design for a new company based in Canberra ACT. We build Rock Retaining Walls, commercial and domestic.
We would like to see designs that use RM letters combine as logo and use stone sandstone or blue rocks. Final design of the business card should communicate strong, wealthy, Rock retaining walls

Target Market(s)

Everybody who needs stone retaining wall in there backyard

Industry/Entity Type

Business

Contact Information for Business Card

RM
Ridgeford Masonry,
Tobin Haraldsen (Stonemason)
Phone/ 0498 315 287
PO Box 3958 Kelvale ACT 2615
E-mail/tharaldsen@oakmail.net.au
www.ridgefordmasonry.com.au

Requirements
Must have
• Letters RM combine as logo. "RIDGEFORD MASONRY" as features
Nice to have
• Rock: Sandstone or bluestone

```html
<!DOCTYPE html>
<html lang="en">
<head>
<meta charset="UTF-8">
<title>Ridgeford Masonry — Business Card</title>
<link rel="stylesheet" href="https://fonts.googleapis.com/css2?family=Cinzel:wght@400&family=Crimson+Pro:wght@400;700&display=swap">
<style>
  :root {
    --paper: #ffffff;
    --ink: #000000;
    --sandstone: #cba357;
    --bluestone: #00c8ff;
    --on-blue: #ffffff;
    --edge: #1a1a1a;
  }
  html, body {
    margin: 0;
    padding: 0;
    width: 1200px;
    height: 740px;
    overflow: hidden;
    background: var(--paper);
  }
  .card {
    position: absolute;
    left: 22px;
    top: 13px;
    width: 1156px;
    height: 712px;
    box-sizing: border-box;
    border: 2px solid var(--edge);
    border-radius: 24px;
    background: var(--paper);
    overflow: hidden;
  }
  .brand-mark {
    position: absolute;
    left: 540px;
    top: 50px;
    width: 72px;
    height: 72px;
    background: var(--sandstone);
  }
  .brand {
    position: absolute;
    left: 0;
    right: 0;
    top: 130px;
    margin: 0;
    text-align: center;
    font-family: "Cinzel", serif;
    font-weight: 400;
    font-size: 84px;
    line-height: 84px;
    color: var(--ink);
    letter-spacing: 0;
  }
  .brand span { display: block; }
  .details {
    position: absolute;
    left: 380px;
    right: -2px;
    top: 339px;
    font-family: "Crimson Pro", serif;
  }
  .identity {
    height: 162px;
    background: var(--sandstone);
    border-top-left-radius: 20px;
    padding: 40px 0 0 28px;
    box-sizing: border-box;
  }
  .identity .name {
    margin: 0;
    font-weight: 700;
    font-size: 54px;
    line-height: 52px;
    color: var(--ink);
  }
  .identity .role {
    margin: 0;
    font-size: 24px;
    line-height: 26px;
    color: var(--ink);
  }
  .contact {
    height: 162px;
    background: var(--bluestone);
    border-bottom-left-radius: 20px;
    padding: 14px 0 0 28px;
    box-sizing: border-box;
    margin: 0;
    list-style: none;
    font-size: 36px;
    line-height: 45px;
    color: var(--on-blue);
  }
</style>
</head>
<body>
  <main class="card">
    <div class="brand-mark" role="img" aria-label="RM logo mark"></div>
    <h1 class="brand"><span>RIDGEFORD</span><span>MASONRY</span></h1>
    <section class="details">
      <div class="identity">
        <p class="name">Tobin Haraldsen</p>
        <p class="role">(Stonemason)</p>
      </div>
      <ul class="contact">
        <li>Phone: 0498 315 287</li>
        <li>PO Box 3958 Kelvale ACT 2615</li>
        <li>tharaldsen@oakmail.net.au</li>
      </ul>
    </section>
  </main>
</body>
</html>
```